banners,restaurant takeaway menu,catering packages for function room and takeaway

We are running indian restaurant in sydney and want to put feather type flags around our boundary.

1. we want to design 5 feather type flag specs
450*1620 mm
shape and image of flag inserted with material
2. Takeaway Menu update
3. Improving layout and redesisgning function menu with packages
4. Improving layout and redsigning of takeaway catering packages

notes

you can use pictures from from restaurant menu or the building pics as available from our restaurant or any better ideas you have

```html
<!DOCTYPE html>
<html lang="en">
<head>
<meta charset="utf-8">
<title>Saffron Leaf Restaurant – Opening Hours Feather Flag</title>
<link href="https://fonts.googleapis.com/css2?family=Oswald:wght@700&family=Open+Sans:wght@400&display=swap" rel="stylesheet">
<style>
  :root {
    --bg: #f2f2f2;
    --saffron: #f29b34;
    --green: #1a8a46;
    --ink: #0d0d0d;
    --rule: #9a9a9a;
    --panel: rgba(255, 255, 255, 0.82);
    --photo-dark: #3a2718;
    --photo-mid: #8a5a32;
    --photo-warm: #c8763a;
  }
  * { margin: 0; padding: 0; box-sizing: border-box; }
  html, body { width: 1200px; height: 4318px; overflow: hidden; background: var(--bg); }
  .flag {
    position: relative;
    width: 1200px;
    height: 4318px;
    background: var(--bg);
    overflow: hidden;
    font-family: "Open Sans", sans-serif;
  }
  .flag__header-art {
    position: absolute;
    left: 0; top: 0;
    width: 1200px; height: 2000px;
  }
  .brand-panel {
    position: absolute;
    left: 388px; top: 560px;
    width: 812px; height: 321px;
    background: var(--panel);
    border-radius: 64px 0 0 64px;
    display: flex;
    flex-direction: column;
    align-items: center;
    justify-content: center;
    padding-left: 20px;
  }
  .brand-panel__name {
    font-family: "Open Sans", sans-serif;
    font-weight: 400;
    font-size: 92px;
    line-height: 1;
    color: var(--ink);
    letter-spacing: -2px;
  }
  .brand-panel__tag {
    margin-top: 18px;
    font-family: "Open Sans", sans-serif;
    font-weight: 400;
    font-size: 30px;
    letter-spacing: 9px;
    color: var(--ink);
  }
  .hours {
    position: absolute;
    left: 0; width: 1200px;
    text-align: center;
  }
  .hours__title {
    font-family: "Oswald", sans-serif;
    font-weight: 700;
    color: var(--saffron);
    font-size: 250px;
    line-height: 250px;
    top: 1842px;
  }
  .hours__meal {
    font-family: "Oswald", sans-serif;
    font-weight: 700;
    color: var(--green);
    font-size: 190px;
    line-height: 190px;
    letter-spacing: 2px;
  }
  .hours__time {
    font-family: "Open Sans", sans-serif;
    font-weight: 400;
    color: var(--ink);
    font-size: 132px;
    line-height: 132px;
  }
  .hours__rule {
    position: absolute;
    left: 190px; width: 820px; height: 3px;
    background: var(--rule);
  }
  .meal-breakfast { top: 2170px; }
  .time-breakfast { top: 2430px; }
  .rule-one { top: 2590px; }
  .meal-lunch { top: 2621px; }
  .time-lunch { top: 2885px; }
  .rule-two { top: 3050px; }
  .meal-dinner { top: 3076px; }
  .time-dinner { top: 3340px; }
</style>
</head>
<body>
<main class="flag">
  <svg class="flag__header-art" viewBox="0 0 1200 2000" xmlns="http://www.w3.org/2000/svg">
    <defs>
      <linearGradient id="dining-tones" x1="0" y1="0" x2="0.3" y2="1">
        <stop offset="0" stop-color="var(--photo-dark)"/>
        <stop offset="0.45" stop-color="var(--photo-mid)"/>
        <stop offset="0.7" stop-color="var(--photo-warm)"/>
        <stop offset="1" stop-color="var(--photo-dark)"/>
      </linearGradient>
    </defs>
    <path role="img" aria-label="Photo of the restaurant dining room with a curry dish, water bottle and glasses on a marble table"
      d="M1130 0 C 700 60, 120 380, 0 1010 L 0 1725 C 300 1560, 700 1560, 1200 1020 L 1200 0 Z"
      fill="url(#dining-tones)"/>
    <path class="swoosh"
      d="M0 1960 C 150 1720, 480 1640, 800 1540 C 1010 1470, 1150 1290, 1200 1190 L 1200 1020 C 1000 1300, 760 1480, 520 1530 C 300 1580, 100 1630, 0 1725 Z"
      fill="var(--saffron)"/>
  </svg>

  <div class="brand-panel">
    <span class="brand-panel__name">Saffron Leaf</span>
    <span class="brand-panel__tag">RESTAURANT</span>
  </div>

  <h1 class="hours hours__title">OPEN FOR</h1>
  <h2 class="hours hours__meal meal-breakfast">BREAKFAST</h2>
  <p class="hours hours__time time-breakfast">9am-11am</p>
  <div class="hours__rule rule-one"></div>
  <h2 class="hours hours__meal meal-lunch">LUNCH</h2>
  <p class="hours hours__time time-lunch">11.30am – 3.00pm</p>
  <div class="hours__rule rule-two"></div>
  <h2 class="hours hours__meal meal-dinner">DINNER</h2>
  <p class="hours hours__time time-dinner">5pm – 10pm</p>
</main>
</body>
</html>
```